Fancy looking Inspection Postcard

Postcard needed for customers to inspect their product once it is delivered. We'll be giving them the steps for inspecting their product and to contact us if any issues arise. Would like to see something that sticks out but uses our company's colors. Would like to see creativity. Possibly utilizing the diamond steel background like we have in our logo.

Target Market(s)

Customers of our manufacturing shop

Industry/Entity Type

Manufacturing - metal wall art, custom products

Requirements
Must have
• our colors and logo
Nice to have
• get creative. i like creativity

```html
<!DOCTYPE html>
<html lang="en">
<head>
<meta charset="utf-8">
<title>Ridgeline Fabrication – Inspection Postcard</title>
<link href="https://fonts.googleapis.com/css2?family=PT+Sans+Narrow:wght@400;700&family=Oswald:wght@500;600&display=swap" rel="stylesheet">
<style>
  :root {
    --page: #efefef;
    --plate-dark: #161616;
    --plate-mid: #3a3a3a;
    --yellow: #fff200;
    --green: #76a544;
    --black: #111111;
    --ink: #141414;
  }
  * { box-sizing: border-box; margin: 0; padding: 0; }
  html, body { width: 1200px; height: 1200px; overflow: hidden; }
  body {
    background: var(--page);
    font-family: "PT Sans Narrow", "Arial Narrow", sans-serif;
    color: var(--ink);
    position: relative;
  }
  .postcard {
    position: absolute;
    left: 232px;
    width: 734px;
    height: 499px;
    overflow: hidden;
    box-shadow: 0 2px 6px rgba(0,0,0,.25);
  }
  .postcard--front { top: 69px; background: var(--green); }
  .postcard--back { top: 628px; background: var(--green); }

  .plate {
    position: absolute;
    background: radial-gradient(ellipse at 50% 55%, var(--plate-mid) 0%, var(--plate-dark) 75%);
  }
  .postcard--front .plate { left: 0; top: 0; width: 734px; height: 214px; }
  .postcard--front .rule { position: absolute; left: 0; top: 214px; width: 734px; height: 6px; background: var(--yellow); }

  .brand {
    position: absolute;
    left: 0; width: 734px; top: 78px;
    display: flex; align-items: center; justify-content: center; gap: 10px;
    font-family: "Oswald", sans-serif; font-weight: 600;
    font-size: 30px; letter-spacing: 1px;
    color: var(--yellow);
  }
  .brand__dot { width: 22px; height: 22px; border-radius: 50%; background: var(--green); }

  .step { position: absolute; width: 323px; height: 110px; }
  .step__tab {
    position: absolute; left: 0; top: 0; width: 279px; height: 95px;
    background: var(--black); border-radius: 0 22px 0 0;
  }
  .step__label {
    position: absolute; left: 4px; top: 6px;
    font-family: "Oswald", sans-serif; font-weight: 600; color: var(--yellow);
    font-size: 17px; line-height: 1;
  }
  .step__num {
    position: absolute; left: 3px; top: 32px;
    font-family: "Oswald", sans-serif; font-weight: 600; color: var(--yellow);
    font-size: 36px; line-height: 1;
  }
  .step__card {
    position: absolute; left: 42px; top: 14px; width: 281px; height: 96px;
    background: var(--yellow); border-radius: 0 14px 14px 14px;
    box-shadow: 0 6px 10px rgba(0,0,0,.35);
  }
  .step__icon {
    position: absolute; left: 0; top: 22px; width: 51px; height: 40px;
    background: var(--black); border-radius: 0 20px 20px 0;
    display: flex; align-items: center; justify-content: center;
  }
  .step__body { position: absolute; left: 58px; top: 10px; right: 4px; }
  .step__title { font-weight: 700; font-size: 21px; line-height: 19px; margin-bottom: 6px; }
  .step__point { font-weight: 700; font-size: 15px; line-height: 21px; padding-left: 8px; text-indent: -8px; }

  .step--1 { left: 38px; top: 231px; }
  .step--2 { left: 38px; top: 353px; }
  .step--3 { left: 375px; top: 231px; }
  .step--4 { left: 375px; top: 353px; }

  .postcard--back .plate { left: 0; top: 0; width: 421px; height: 499px; }
  .postcard--back .divider { position: absolute; left: 421px; top: 0; width: 7px; height: 499px; background: var(--yellow); }

  .contact {
    position: absolute; left: 33px; top: 43px; width: 369px; height: 413px;
    background: var(--yellow); border-radius: 0 16px 16px 16px;
    padding: 10px 0 0 19px;
    box-shadow: -8px 8px 12px rgba(0,0,0,.45);
  }
  .contact__lead { font-size: 20px; line-height: 22px; }
  .contact__value { font-weight: 700; font-size: 25px; line-height: 30px; margin-bottom: 5px; }
  .contact__heading { font-weight: 700; font-size: 36px; line-height: 40px; margin-top: 22px; margin-bottom: 4px; }
  .contact__text { font-size: 22px; line-height: 28px; }
  .contact__text strong { font-weight: 700; }

  .stamp { position: absolute; left: 592px; top: 35px; width: 106px; height: 76px; border: 1.5px solid var(--black); }
  .address-line { position: absolute; left: 445px; width: 253px; height: 1.5px; background: var(--black); }

  .brand--small {
    position: absolute; left: 470px; width: 200px; top: 406px;
    display: flex; align-items: center; justify-content: center; gap: 6px;
    font-family: "Oswald", sans-serif; font-weight: 600; font-size: 15px;
    color: var(--black);
  }
  .brand--small .brand__dot { width: 12px; height: 12px; background: var(--yellow); }
</style>
</head>
<body>

<section class="postcard postcard--front">
  <div class="plate" role="img" aria-label="Diamond steel plate texture"></div>
  <div class="rule"></div>
  <div class="brand"><span class="brand__dot"></span>RIDGELINE FABRICATION</div>

  <article class="step step--1">
    <div class="step__tab"><span class="step__label">STEP</span><span class="step__num">01</span></div>
    <div class="step__card">
      <div class="step__icon">
        <svg width="24" height="24" viewBox="0 0 24 24" fill="none" stroke="#fff200" stroke-width="2"><circle cx="14" cy="10" r="6"/><path d="M9.5 14.5 3 21"/><path d="m11.5 10 2 2 3-4"/></svg>
      </div>
      <div class="step__body">
        <h2 class="step__title">Inspect general shape</h2>
        <p class="step__point">- Is it what you expected?</p>
        <p class="step__point">- Is it bent, disoriented?</p>
      </div>
    </div>
  </article>

  <article class="step step--2">
    <div class="step__tab"><span class="step__label">STEP</span><span class="step__num">02</span></div>
    <div class="step__card">
      <div class="step__icon">
        <svg width="24" height="24" viewBox="0 0 24 24" fill="none" stroke="#fff200" stroke-width="2"><circle cx="11" cy="10" r="7"/><path d="M16 15l6 6"/><path d="M8 8h6M8 11h6"/></svg>
      </div>
      <div class="step__body">
        <h2 class="step__title">Inspect the welds if there are any</h2>
        <p class="step__point">- Do they look clean?</p>
        <p class="step__point">- Are there any gaps?</p>
      </div>
    </div>
  </article>

  <article class="step step--3">
    <div class="step__tab"><span class="step__label">STEP</span><span class="step__num">03</span></div>
    <div class="step__card">
      <div class="step__icon">
        <svg width="24" height="24" viewBox="0 0 24 24" fill="none" stroke="#fff200" stroke-width="2.2"><path d="M20 12a8 8 0 1 1-3-6.2"/><path d="m8 12 3 3 6-7"/></svg>
      </div>
      <div class="step__body">
        <h2 class="step__title">Inspect the finish</h2>
        <p class="step__point">- Are there any areas not finished?</p>
        <p class="step__point">- Are the colors what you expected?</p>
      </div>
    </div>
  </article>

  <article class="step step--4">
    <div class="step__tab"><span class="step__label">STEP</span><span class="step__num">04</span></div>
    <div class="step__card">
      <div class="step__icon">
        <svg width="24" height="24" viewBox="0 0 24 24" fill="none" stroke="#fff200" stroke-width="1.8"><rect x="9" y="3" width="12" height="18" rx="1"/><path d="m12 8 1.5 1.5L16 7M12 14l1.5 1.5L16 13"/><circle cx="5" cy="14" r="3"/></svg>
      </div>
      <div class="step__body">
        <h2 class="step__title">Check for functionality</h2>
        <p class="step__point">- Does it work the way you want it to?</p>
        <p class="step__point">- Is it what you expected?</p>
      </div>
    </div>
  </article>
</section>

<section class="postcard postcard--back">
  <div class="plate" role="img" aria-label="Diamond steel plate texture"></div>
  <div class="divider"></div>

  <div class="contact">
    <p class="contact__lead">E-mail us at</p>
    <p class="contact__value">orders@ridgelinefab.com</p>
    <p class="contact__lead">Shoot us a text</p>
    <p class="contact__value">(555) 204-0101</p>
    <p class="contact__lead">Reach out via</p>
    <p class="contact__value">www.ridgelinefab.com/contact</p>
    <h2 class="contact__heading">Did we do a good job?</h2>
    <p class="contact__text">If you think so, leave us a review on <strong>Rateway</strong>?</p>
    <p class="contact__text">If not, please let us know-</p>
    <p class="contact__value">info@ridgelinefab.com</p>
    <p class="contact__text">or call us</p>
    <p class="contact__value">555-476-0199</p>
  </div>

  <div class="stamp"></div>
  <div class="address-line" style="top:188px"></div>
  <div class="address-line" style="top:229px"></div>
  <div class="address-line" style="top:266px"></div>
  <div class="address-line" style="top:307px"></div>
  <div class="address-line" style="top:345px"></div>

  <div class="brand brand--small"><span class="brand__dot"></span>RIDGELINE FABRICATION</div>
</section>

</body>
</html>
```